Strong, Clean Book Design Needed for "The Lantern Keeper"

I need a strong, clean, masculine cover of a book that focuses on helping men restore honor to what it means to be a good husband. (I also need a back cover and spine done as well). I would like the cover to be either a white, red, or black cover. I have attached 3 books that I would like to use as examples to model after. I also attached a word document to show the potential layouts I would like to see and how that parallel the example covers.

Specs:
- Book is 150 pages long
- Size is 5.25 x 8

Target Market(s)

Christian men who are married or looking to be married.

Font styles to use
Serif
Sans Serif

Colors
ec1f27
f04a50
ffffff
000000
1b1b1b
757575

Requirements
Must have
• - A design that resembles/has a similar feel to one of the three examples that are attached and laid out similarly to one of the 3 designs in the word doc "3 Book Designs"
• - These elements on the front cover: Title: The Lantern Keeper, Subtitle: Restoring the honor of a Christ-centered marriage, Author Name: Dale Forsby
• - A strong design that is simple yet creative.
• - Strong masculine font that is bold but not too flashy
• - Red should be included either as the title font color or as the overall cover color.
• - The back of the book should have the attached file "Back of the book" text on the back
Nice to have
• - A color contrast, like a strip of another color (see "example 3" attached file) across the front for the subtitle or the author name.
• - Including the attached sword file as a somewhat transparent image on the cover, but absolutely not necessary.
• - If there is going to be any highlighting of words in the subtitle, they should be the word "honor" and "Christ-centered"
Should not have
• Any religious symbols, such as a cross.

```html
<!DOCTYPE html>
<html lang="en">
<head>
<meta charset="utf-8">
<title>The Lantern Keeper – Book Cover Wrap</title>
<link rel="stylesheet" href="https://fonts.googleapis.com/css2?family=Cinzel:wght@400;700&family=Crimson+Text:ital,wght@0,400;0,700;1,400&display=swap">
<style>
  :root {
    --paper: #e8e6d8;
    --paper-dark: #dcdaca;
    --title-red: #a81c20;
    --band-red: #a91b1e;
    --ink: #1b1b1b;
    --band-text: #f4ece6;
    --art-dark: #3a3034;
    --art-red: #b3373b;
    --art-light: #c9c6bc;
  }
  * { margin: 0; padding: 0; box-sizing: border-box; }
  html, body { width: 1200px; height: 886px; overflow: hidden; }
  body { background: var(--paper); }

  .book-wrap {
    position: relative;
    width: 1200px;
    height: 886px;
    overflow: hidden;
    background:
      repeating-linear-gradient(0deg, rgba(0,0,0,0.018) 0 1px, transparent 1px 3px),
      repeating-linear-gradient(90deg, rgba(0,0,0,0.015) 0 1px, transparent 1px 4px),
      radial-gradient(ellipse at 50% 40%, var(--paper) 0%, var(--paper-dark) 100%);
    color: var(--ink);
  }

  /* Back cover */
  .back-copy {
    position: absolute;
    left: 30px;
    width: 520px;
    text-align: center;
    white-space: nowrap;
    font-family: "Crimson Text", Georgia, serif;
    font-size: 15.8px;
    line-height: 20.3px;
    color: var(--ink);
  }
  .back-hook   { top: 38px; }
  .back-intro  { top: 78px; }
  .back-pitch  { top: 241px; }
  .back-call   { top: 485px; }
  .back-close  { top: 566px; }
  .back-author { top: 630px; }

  /* Spine */
  .spine-title, .spine-author {
    position: absolute;
    writing-mode: vertical-rl;
    color: var(--ink);
    white-space: nowrap;
  }
  .spine-title {
    left: 584px;
    top: 34px;
    font-family: "Cinzel", Georgia, serif;
    font-size: 27px;
    line-height: 28px;
  }
  .spine-author {
    left: 587px;
    top: 640px;
    font-family: "Crimson Text", Georgia, serif;
    font-size: 21px;
    line-height: 22px;
  }

  /* Front cover */
  .front-title, .front-subtitle { font-weight: 400; }
  .front-title span, .front-subtitle span {
    position: absolute;
    left: 645px;
    white-space: nowrap;
    line-height: 1;
    font-family: "Cinzel", Georgia, serif;
  }
  .front-title span { color: var(--title-red); }
  .title-the     { top: 32px;  font-size: 54px; }
  .title-lantern { top: 94px;  font-size: 82px; }
  .title-keeper  { top: 182px; font-size: 82px; }

  .front-subtitle span { color: var(--ink); left: 647px; }
  .sub-restoring  { top: 294px; font-size: 35px; }
  .sub-honor-line { top: 331px; font-size: 36px; }
  .sub-honor-line em {
    font-family: "Crimson Text", Georgia, serif;
    font-style: italic;
    font-size: 30px;
  }
  .sub-honor-line strong { font-weight: 700; font-size: 37px; }
  .sub-christ   { top: 369px; font-weight: 700; font-size: 37px; }
  .sub-marriage { top: 409px; font-size: 30px; }

  .sword-art {
    position: absolute;
    left: 0;
    top: 0;
  }

  .author-band {
    position: absolute;
    left: 0;
    top: 762px;
    width: 1200px;
    height: 70px;
    background: var(--band-red);
  }
  .author-name {
    position: absolute;
    left: 784px;
    top: 762px;
    height: 70px;
    line-height: 70px;
    font-family: "Crimson Text", Georgia, serif;
    font-weight: 700;
    font-size: 44px;
    letter-spacing: 1px;
    white-space: nowrap;
    color: var(--band-text);
  }
</style>
</head>
<body>
<main class="book-wrap">

  <section class="back-cover">
    <p class="back-copy back-hook">Do you have what it takes to be a Lantern Keeper?</p>
    <p class="back-copy back-intro">
      The samurai were fearsome Japanese warriors known for their discipline,<br>
      loyalty, and strict adherence to their code of honor, bushido. Along with<br>
      their ferocity on the battlefield, they also embodied the heart and<br>
      sacrifice of “those who serve,” the meaning of the word samurai.<br>
      The samurai lived, and more importantly, died by the honor that charac-<br>
      terized these ideals. The samurai way of life transformed the nation,<br>
      culture, and moral code of Japan, and continues to do so to this day…
    </p>
    <p class="back-copy back-pitch">
      The Lantern Keeper is more than just an interesting read: it is a<br>
      radically Christ-centered approach to marriage. Dale Forsby recaptures<br>
      what it means to be a man and an effective leader in a marriage by<br>
      simply, but powerfully, laying out the Biblical qualities found in Ephe-<br>
      sians 5 that God calls husbands to embody. With a fresh and unique<br>
      perspective, Dale parallels how samurai warriors once lived and how<br>
      godly husbands should live in a way that restores and highlights the<br>
      honor, sacrifice, and purpose of marriage. This book will undoubtedly<br>
      shift the way men view and function in their role as a husband and gives<br>
      them practical nuts and bolts suggestions for<br>
      day-to-day success as a husband.
    </p>
    <p class="back-copy back-call">
      This is a wake-up call to all husbands everywhere: be the man and the<br>
      husband God has called you to be. Although it is not easy,<br>
      it is guaranteed to transform your life… and your marriage!
    </p>
    <p class="back-copy back-close">
      Embrace the call of a truly Christ-centered marriage.<br>
      Embrace the way of the Lantern Keeper.
    </p>
    <p class="back-copy back-author">
      DALE FORSBY is the Microchurch Pastor at the Ironwood Chapel in<br>
      Millbrook, Ohio where he has a heart for marriage as well as multiplying<br>
      disciples and churches. He has a fierce love for and<br>
      has been married to his wife, Joanna, for over a decade.<br>
      They have two beautiful daughters, Miriam and Rosalie.
    </p>
  </section>

  <section class="spine">
    <p class="spine-title">The Lantern Keeper</p>
    <p class="spine-author">Dale Forsby</p>
  </section>

  <section class="front-cover">
    <h1 class="front-title">
      <span class="title-the">The</span>
      <span class="title-lantern">Lantern</span>
      <span class="title-keeper">Keeper</span>
    </h1>
    <h2 class="front-subtitle">
      <span class="sub-restoring">Restoring</span>
      <span class="sub-honor-line"><em>the</em> <strong>HONOR</strong> <em>of a</em></span>
      <span class="sub-christ">CHRIST-CENTERED</span>
      <span class="sub-marriage">MARRIAGE</span>
    </h2>

    <svg class="sword-art" width="1200" height="886" viewBox="0 0 1200 886" role="img" aria-label="Artwork area: a katana with a red ribbon tied below the guard, angled across the front cover">
      <defs>
        <linearGradient id="artTone" x1="0" y1="0" x2="0" y2="1">
          <stop offset="0" stop-color="var(--art-dark)" stop-opacity="0.55"/>
          <stop offset="0.5" stop-color="var(--art-red)" stop-opacity="0.4"/>
          <stop offset="1" stop-color="var(--art-light)" stop-opacity="0.5"/>
        </linearGradient>
      </defs>
      <rect x="-42" y="-430" width="84" height="880" rx="42" fill="url(#artTone)" transform="translate(1036 500) rotate(19.7)"/>
    </svg>

    <div class="author-band"></div>
    <p class="author-name">Dale Forsby</p>
  </section>

</main>
</body>
</html>
```